Shampoo and Shower Gel Packaging Design

I need a new packaging design for a men shampoo and shower gel bottle. The packaging must me black (black bottle/package) and the logo should be also monochrom.
For example, black matte bottle and black shiny logo on the packaging (not mandatory).
the design must contain maximum 3 colors.
1. black
2. white (text)
3. grey/dark blue/dark green (colors will be the difference between products parfumes/smell/scences.

Design must be minimalist/elegant/discrete.
Updates

Please check the photos i added for pure inspiration.

Target Market(s)

brand exclusively for MEN - premium clients

Industry/Entity Type

Cosmetics

Font styles to use
Sans Serif

Colors
1b1b1b
5c5c5c
aaaaaa
ffffff
3176b5

Requirements
Must have
• black background
• minimalist design

```html
<!DOCTYPE html>
<html lang="en">
<head>
<meta charset="UTF-8">
<title>Varden Cosmetics — Shampoo for Men</title>
<link rel="stylesheet" href="https://fonts.googleapis.com/css2?family=Josefin+Sans:wght@300;400&family=Montserrat:wght@300;400&family=Playfair+Display:wght@900&display=swap">
<style>
  :root {
    --field-center: #3a3a3a;
    --field-edge: #0a0a0a;
    --bottle-black: #101010;
    --collar-grey: #aaaaaa;
    --label-white: #ffffff;
    --accent-grey: #5c5c5c;
    --soft-grey: #aaaaaa;
  }
  * { margin: 0; padding: 0; box-sizing: border-box; }
  html, body {
    width: 1200px;
    height: 980px;
    overflow: hidden;
    background: var(--field-edge);
  }
  .stage {
    position: relative;
    width: 1200px;
    height: 980px;
    background: radial-gradient(ellipse 620px 560px at 600px 480px, var(--field-center) 0%, #1b1b1b 60%, var(--field-edge) 100%);
    color: var(--label-white);
  }
  .bottle {
    position: absolute;
    left: 0;
    top: 0;
  }
  .brand {
    position: absolute;
    left: 493px;
    width: 234px;
    top: 460px;
    text-align: center;
  }
  .brand-name {
    display: block;
    font-family: "Montserrat", sans-serif;
    font-weight: 300;
    font-size: 20px;
    letter-spacing: 0.5em;
    padding-left: 0.5em;
    line-height: 1;
    color: var(--label-white);
  }
  .brand-sub {
    display: block;
    margin-top: 5px;
    font-family: "Montserrat", sans-serif;
    font-weight: 400;
    font-size: 6px;
    letter-spacing: 0.45em;
    padding-left: 0.45em;
    color: var(--soft-grey);
  }
  .product-title {
    position: absolute;
    left: 556px;
    top: 600px;
    width: 160px;
  }
  .product-name {
    display: block;
    font-family: "Playfair Display", serif;
    font-weight: 900;
    font-size: 34px;
    line-height: 1;
    letter-spacing: -0.01em;
    transform: scaleX(0.84);
    transform-origin: left center;
    white-space: nowrap;
    color: var(--label-white);
  }
  .product-line {
    display: flex;
    align-items: flex-start;
    gap: 2px;
    margin-top: 2px;
  }
  .product-bar {
    width: 33px;
    height: 7px;
    margin-top: 2px;
    background: var(--accent-grey);
  }
  .product-audience {
    font-family: "Josefin Sans", sans-serif;
    font-weight: 300;
    font-size: 25px;
    line-height: 1;
    white-space: nowrap;
    color: var(--label-white);
  }
  .volume {
    position: absolute;
    left: 493px;
    width: 234px;
    top: 760px;
    text-align: center;
    padding-left: 34px;
    font-family: "Josefin Sans", sans-serif;
    font-weight: 300;
    font-size: 16px;
    color: var(--label-white);
  }
</style>
</head>
<body>
  <main class="stage">
    <svg class="bottle" width="1200" height="980" viewBox="0 0 1200 980" aria-hidden="true">
      <rect class="pump-head" x="500" y="203" width="166" height="24" rx="6" fill="var(--label-white)"/>
      <rect class="pump-stem" x="578" y="225" width="42" height="34" fill="var(--label-white)"/>
      <rect class="pump-collar" x="553" y="257" width="104" height="78" rx="4" fill="var(--collar-grey)"/>
      <rect class="bottle-body" x="493" y="330" width="234" height="513" rx="30" fill="var(--bottle-black)"/>
    </svg>

    <div class="brand">
      <span class="brand-name">VARDEN</span>
      <span class="brand-sub">COSMETICS</span>
    </div>

    <div class="product-title">
      <span class="product-name">SHAMPOO</span>
      <div class="product-line">
        <span class="product-bar"></span>
        <span class="product-audience">FOR MEN</span>
      </div>
    </div>

    <p class="volume">200ml</p>
  </main>
</body>
</html>
```